Medical Marihuana Ziplock Bag Mockup Design

We seek skilled and professional designer for medical marihuana ziplock bag packaging design. We need a modern, minimal, clean Design with the name productname: Plumo - Endproduct will be a ziplock bag (see attachment) samples.
Product may but must not contain a cannabis leaf in Design7Logo

Target Market(s)

young audience

Industry/Entity Type

Medical

Logo Text

P L U M O

Font styles to use
Serif
Sans Serif

Colors
9bcb3c
abd037
cadf82
ffc214
fece3e
fee18a
6b449b
886aae
b8a6cd

Requirements
Nice to have
• Can but must not contain a minimal cannabis leaf as abstract sign

```html
<!DOCTYPE html>
<html lang="en">
<head>
<meta charset="utf-8">
<title>Plumo – Bag Label</title>
<link href="https://fonts.googleapis.com/css2?family=Quicksand:wght@300;500;700&display=swap" rel="stylesheet">
<style>
  :root {
    --paper: #ffffff;
    --ink: #333333;
    --muted: #b3b3b3;
    --purple: #6b449b;
    --green: #a6cd3a;
    --outline: #5a5a5a;
    --rule: #d8cfe6;
  }
  html, body {
    margin: 0;
    padding: 0;
    overflow: hidden;
    background: var(--paper);
  }
  .canvas {
    position: relative;
    width: 848px;
    height: 1200px;
    overflow: hidden;
    background: var(--paper);
    font-family: "Quicksand", sans-serif;
  }
  .option {
    position: absolute;
    top: 86px;
    width: 220px;
    text-align: center;
  }
  .option--one { left: 180px; }
  .option--two { left: 458px; }
  .option__label {
    font-weight: 700;
    font-size: 20px;
    letter-spacing: 1px;
    color: var(--muted);
  }
  .brand {
    display: flex;
    flex-direction: column;
    align-items: center;
  }
  .brand__dot {
    border-radius: 50%;
    background: var(--purple);
  }
  .brand__name {
    font-weight: 300;
    color: var(--ink);
    line-height: 1;
  }
  .option .brand { margin-top: 18px; }
  .option .brand__dot { width: 74px; height: 74px; }
  .option .brand__name { font-size: 64px; margin-top: 14px; }

  .label-shape {
    position: absolute;
    left: 0;
    top: 0;
  }
  .label-brand {
    position: absolute;
    left: 223px;
    top: 392px;
    width: 416px;
  }
  .label-brand .brand__dot { width: 112px; height: 112px; }
  .label-brand .brand__name { font-size: 90px; margin-top: 14px; }

  .label-copy {
    position: absolute;
    left: 288px;
    top: 672px;
    width: 291px;
    border-top: 1.5px solid var(--rule);
    border-bottom: 1.5px solid var(--rule);
    padding: 30px 0 32px;
    text-align: center;
    color: var(--paper);
    font-weight: 500;
    font-size: 21px;
    line-height: 29px;
  }
  .label-weight {
    position: absolute;
    left: 223px;
    top: 985px;
    width: 416px;
    text-align: center;
    color: var(--paper);
    font-weight: 700;
    font-size: 32px;
  }
</style>
</head>
<body>
<div class="canvas">

  <div class="option option--one">
    <div class="option__label">OPT 1</div>
    <div class="brand">
      <div class="brand__dot"></div>
      <div class="brand__name">plumo</div>
    </div>
  </div>

  <div class="option option--two">
    <div class="option__label">OPT 2</div>
    <div class="brand">
      <div class="brand__dot"></div>
      <div class="brand__name">plumo</div>
    </div>
  </div>

  <svg class="label-shape" width="848" height="1200" viewBox="0 0 848 1200" aria-hidden="true">
    <rect x="223.5" y="358.5" width="415" height="264" fill="var(--paper)" stroke="var(--outline)" stroke-width="1"/>
    <path d="M223 985 L431 1070 L639 985 L639 1010 L431 1088 L223 1010 Z" fill="var(--green)" stroke="var(--outline)" stroke-width="1"/>
    <path d="M223 622 H639 V985 L431 1070 L223 985 Z" fill="var(--purple)"/>
  </svg>

  <div class="label-brand">
    <div class="brand">
      <div class="brand__dot"></div>
      <div class="brand__name">plumo</div>
    </div>
  </div>

  <div class="label-copy">
    Mauris gravida elit porttitor laoreet luctus. In hac habitasse platea dictumst. Aenean leo mi, tempor ut purus in, tincidunt accumsan odio. Cras viverra lorem in metus luctus porttitor.
  </div>

  <div class="label-weight">10g</div>

</div>
</body>
</html>
```